Rack Flyer for Willowmere Dementia

We need a rack flyer design providing information on services we offer, fees and relevant contact information. Using company branding (logo, font and colours). Must be provided in a format that is easily edited for ongoing use.

For DL size (99 x 210mm)

```html
<!DOCTYPE html>
<html lang="en">
<head>
<meta charset="utf-8">
<title>Willowmere Dementia – Rack Flyer</title>
<link rel="stylesheet" href="https://fonts.googleapis.com/css2?family=Poppins:wght@400;500;600;700&family=Heebo:wght@700;800&family=Sacramento&display=swap">
<style>
:root{
  --navy:#1f1c6e;
  --orange:#f2a024;
  --orange-deep:#ec9413;
  --grey-box:#ececec;
  --ink:#1d1d2b;
  --page:#e4e4e6;
  --white:#ffffff;
}
*{box-sizing:border-box;margin:0;padding:0}
html,body{width:1200px;height:2232px;overflow:hidden}
body{background:var(--page);font-family:'Poppins',sans-serif;color:var(--ink);position:relative}
.panel{position:absolute;top:543px;width:540px;height:1146px;background:var(--white);overflow:hidden;box-shadow:0 6px 18px rgba(0,0,0,.12)}
.panel--front{left:40px}
.panel--back{left:620px}
.layer{position:absolute;left:0;top:0;width:540px;height:1146px}
.abs{position:absolute}
.brand{font-family:'Poppins',sans-serif;font-weight:700;color:var(--navy);font-size:30px;letter-spacing:-.3px;white-space:nowrap;display:flex;align-items:center;gap:10px}
.brand-dot{width:22px;height:22px;border-radius:50%;background:var(--orange);display:inline-block}

/* front */
.hero-photo{left:0;top:105px;width:540px;height:470px;background:linear-gradient(160deg,#e9e4dd 0%,#b58a66 35%,#6b4a36 55%,#e1a92c 80%,#f0b43a 100%)}
.circle-photo{left:48px;top:368px;width:196px;height:196px;border-radius:50%;border:8px solid #f4b54c;background:radial-gradient(circle at 50% 40%,#dfe9ee,#9fb2bd 60%,#4a5660)}
.headline{left:40px;top:580px;font-family:'Heebo',sans-serif;font-weight:800;color:var(--navy);font-size:60px;line-height:56px;letter-spacing:-.5px;white-space:nowrap}
.script{font-family:'Sacramento',cursive;color:var(--orange);font-weight:400;letter-spacing:0}
.headline .script{font-size:46px}
.rule{left:40px;top:711px;width:380px;height:1px;background:#9a9aa8}
.section-title{left:42px;top:724px;font-family:'Heebo',sans-serif;font-weight:700;color:var(--navy);font-size:31px;white-space:nowrap}
.section-title .script{font-size:36px}
.service-list{list-style:none;font-size:13.6px;line-height:15px;font-weight:500;color:var(--ink)}
.service-list li{position:relative;padding-left:21px}
.tick{position:absolute;left:0;top:1px;width:14px;height:14px}
.list-left{left:42px;top:787px;width:215px}
.list-right{left:267px;top:787px;width:260px}
.list-left li{margin-bottom:17px}
.list-right li{margin-bottom:15px}

.phone-pill{height:46px;border-radius:23px;background:var(--orange);display:flex;align-items:center;gap:10px;padding:0 18px 0 7px;font-family:'Poppins',sans-serif;font-weight:700;color:var(--navy);font-size:31px;letter-spacing:2px;white-space:nowrap}
.phone-icon{width:34px;height:34px;border-radius:50%;background:var(--white);display:flex;align-items:center;justify-content:center}
.footer-band{left:0;width:540px;background:var(--navy)}
.contact-line{left:0;width:540px;text-align:center;color:var(--white);font-size:14px;font-weight:500;display:flex;justify-content:center;align-items:center;gap:6px;white-space:nowrap}
.contact-line svg{flex:none}

/* back */
.intro{left:38px;top:112px;width:464px;font-size:14.2px;line-height:18.5px;color:var(--ink);text-align:justify}
.intro p+p{margin-top:18px}
.brand-rule{top:76px;height:1.5px;background:var(--navy)}
.fees-title{left:0;width:540px;top:468px;text-align:center;font-family:'Heebo',sans-serif;font-weight:700;color:var(--navy);font-size:33px}
.fees-title .script{font-size:40px}
.fee-card{border-radius:7px;overflow:hidden;border:2px solid var(--navy);display:flex;flex-direction:column}
.fee-card--gold{border-color:var(--orange)}
.fee-label{flex:1;background:var(--grey-box);display:flex;align-items:center;justify-content:center;text-align:center;font-size:13px;line-height:15.5px;color:var(--ink);padding:0 6px}
.fee-price{height:36px;background:var(--navy);color:var(--white);font-weight:700;font-size:21px;display:flex;align-items:center;justify-content:center}
.fee-card--gold .fee-price{background:var(--orange)}
.per-term{font-size:7px;line-height:7px;font-weight:500;display:inline-block;text-align:center;margin:0 2px}
.coverage{left:36px;top:822px;width:466px;font-size:14.2px;line-height:18.5px;text-align:justify}
.reach-out{left:0;width:540px;top:960px;text-align:center;font-weight:600;color:var(--ink);font-size:19px;line-height:23px}
</style>
</head>
<body>

<!-- FRONT -->
<section class="panel panel--front" aria-label="Flyer front">
  <div class="abs hero-photo" role="img" aria-label="Photograph of an older couple, the woman holding her head in distress while her partner comforts her"></div>

  <svg class="layer" viewBox="0 0 540 1146" aria-hidden="true">
    <rect x="0" y="0" width="540" height="108" fill="#f6f6f6"/>
    <path d="M0 330 C60 420 150 470 250 470 C330 470 420 520 540 600 L540 640 C430 560 330 520 240 525 C130 530 50 470 0 420 Z" fill="var(--orange)"/>
    <path d="M0 360 C50 430 140 490 240 492 C340 494 430 540 540 640 L540 1146 L0 1146 Z" fill="var(--white)"/>
    <path d="M0 380 C40 440 120 500 220 510 C330 520 430 560 500 640 C530 680 545 730 540 760 L540 760 C520 700 470 640 400 600 C330 560 260 560 210 560 L200 540 C120 530 40 460 0 410 Z" fill="var(--navy)"/>
    <path d="M250 495 C350 500 440 540 500 610 C540 660 550 720 540 780 C530 740 505 700 470 690 C475 650 440 600 380 570 C330 545 280 540 240 540 Z" fill="var(--navy)"/>
    <path d="M505 820 C500 770 490 740 470 700" stroke="var(--navy)" stroke-width="6" fill="none"/>
    <polygon points="487,657 494,674 512,675 498,686 503,703 487,693 471,703 476,686 462,675 480,674" fill="var(--orange)"/>
  </svg>

  <div class="abs circle-photo" role="img" aria-label="Photograph of a clinician consulting with a patient in a bright office"></div>

  <div class="abs brand" style="left:0;width:540px;top:62px;justify-content:center"><span class="brand-dot"></span>Willowmere Dementia</div>

  <h1 class="abs headline">Navigating<br>Dementia<span class="script"> Together</span></h1>
  <div class="abs rule"></div>
  <h2 class="abs section-title">SERVICES <span class="script">Offered</span></h2>

  <ul class="abs service-list list-left">
    <li><svg class="tick" viewBox="0 0 14 14"><circle cx="7" cy="7" r="7" fill="#1f1c6e"/><path d="M3.8 7.2l2.1 2.1 4.3-4.4" stroke="#fff" stroke-width="1.8" fill="none"/></svg>Comprehensive Dementia<br>Assessment</li>
    <li><svg class="tick" viewBox="0 0 14 14"><circle cx="7" cy="7" r="7" fill="#1f1c6e"/><path d="M3.8 7.2l2.1 2.1 4.3-4.4" stroke="#fff" stroke-width="1.8" fill="none"/></svg>Cognitive/Perceptual<br>Screening</li>
    <li><svg class="tick" viewBox="0 0 14 14"><circle cx="7" cy="7" r="7" fill="#1f1c6e"/><path d="M3.8 7.2l2.1 2.1 4.3-4.4" stroke="#fff" stroke-width="1.8" fill="none"/></svg>Home Safety Audit<br>(Home modifications and<br>adaptive equipment aids)</li>
    <li><svg class="tick" viewBox="0 0 14 14"><circle cx="7" cy="7" r="7" fill="#1f1c6e"/><path d="M3.8 7.2l2.1 2.1 4.3-4.4" stroke="#fff" stroke-width="1.8" fill="none"/></svg>Caregiver Education &amp;<br>Support</li>
    <li><svg class="tick" viewBox="0 0 14 14"><circle cx="7" cy="7" r="7" fill="#1f1c6e"/><path d="M3.8 7.2l2.1 2.1 4.3-4.4" stroke="#fff" stroke-width="1.8" fill="none"/></svg>Falls Prevention Strategies</li>
  </ul>
  <ul class="abs service-list list-right">
    <li><svg class="tick" viewBox="0 0 14 14"><circle cx="7" cy="7" r="7" fill="#1f1c6e"/><path d="M3.8 7.2l2.1 2.1 4.3-4.4" stroke="#fff" stroke-width="1.8" fill="none"/></svg>Personalised Care Planning</li>
    <li><svg class="tick" viewBox="0 0 14 14"><circle cx="7" cy="7" r="7" fill="#1f1c6e"/><path d="M3.8 7.2l2.1 2.1 4.3-4.4" stroke="#fff" stroke-width="1.8" fill="none"/></svg>Preparation for future disease<br>progression</li>
    <li><svg class="tick" viewBox="0 0 14 14"><circle cx="7" cy="7" r="7" fill="#1f1c6e"/><path d="M3.8 7.2l2.1 2.1 4.3-4.4" stroke="#fff" stroke-width="1.8" fill="none"/></svg>Case Management Support</li>
    <li><svg class="tick" viewBox="0 0 14 14"><circle cx="7" cy="7" r="7" fill="#1f1c6e"/><path d="M3.8 7.2l2.1 2.1 4.3-4.4" stroke="#fff" stroke-width="1.8" fill="none"/></svg>Check-in/monitoring visits<br>for clients with limited social<br>support</li>
    <li><svg class="tick" viewBox="0 0 14 14"><circle cx="7" cy="7" r="7" fill="#1f1c6e"/><path d="M3.8 7.2l2.1 2.1 4.3-4.4" stroke="#fff" stroke-width="1.8" fill="none"/></svg>Cognitive Stimulation<br>Therapy (group program<br>for individuals with mild<br>moderate stage dementia)</li>
  </ul>

  <div class="abs footer-band" style="top:1041px;height:105px"></div>
  <div class="abs phone-pill" style="left:111px;top:1027px">
    <span class="phone-icon"><svg width="20" height="20" viewBox="0 0 24 24"><path d="M6.6 10.8a15 15 0 0 0 6.6 6.6l2.2-2.2a1 1 0 0 1 1-.25 11.4 11.4 0 0 0 3.6.57 1 1 0 0 1 1 1V20a1 1 0 0 1-1 1A17 17 0 0 1 3 4a1 1 0 0 1 1-1h3.5a1 1 0 0 1 1 1c0 1.25.2 2.45.57 3.57a1 1 0 0 1-.25 1Z" fill="#1f1c6e"/></svg></span>(441) 555 0142
  </div>
  <div class="abs contact-line" style="top:1093px">
    <svg width="15" height="11" viewBox="0 0 15 11"><rect width="15" height="11" rx="1" fill="#f2a024"/><path d="M0 1l7.5 5L15 1" stroke="#1f1c6e" stroke-width="1.3" fill="none"/></svg>info@willowmeredementia.bm
    <svg width="15" height="15" viewBox="0 0 16 16" style="margin-left:6px"><circle cx="8" cy="8" r="7" stroke="#f2a024" stroke-width="1.4" fill="none"/><ellipse cx="8" cy="8" rx="3" ry="7" stroke="#f2a024" stroke-width="1.2" fill="none"/><path d="M1 8h14M2.5 4.5h11M2.5 11.5h11" stroke="#f2a024" stroke-width="1.1"/></svg>www.willowmeredementia.bm
  </div>
</section>

<!-- BACK -->
<section class="panel panel--back" aria-label="Flyer back">
  <svg class="layer" viewBox="0 0 540 1146" aria-hidden="true">
    <rect x="0" y="0" width="540" height="460" fill="var(--orange)"/>
    <path d="M0 460 C120 395 260 380 380 400 C450 412 500 410 540 395 L540 1146 L0 1146 Z" fill="var(--orange-deep)"/>
    <path d="M0 470 C110 390 250 385 370 415 C440 432 500 430 540 412 L540 440 C490 470 420 470 360 455 C250 430 130 440 50 500 C30 515 20 530 10 545 Z" fill="var(--navy)"/>
    <path d="M10 545 C40 480 140 440 260 445 C370 450 460 500 540 465 L540 1146 L0 1146 L0 560 Z" fill="var(--white)"/>
    <path d="M540 430 C470 470 400 470 340 462 C420 490 490 480 540 455 Z" fill="var(--orange)"/>
    <path d="M60 470 C90 480 95 520 85 590 C80 540 70 505 40 490 Z" fill="var(--navy)"/>
    <polygon points="43,484 50,501 68,502 54,513 59,530 43,520 27,530 32,513 18,502 36,501" fill="var(--orange)"/>
  </svg>

  <div class="abs brand-rule" style="left:38px;width:86px"></div>
  <div class="abs brand-rule" style="left:416px;width:86px"></div>
  <div class="abs brand" style="left:0;width:540px;top:56px;justify-content:center;font-size:24px">Willowmere Dementia</div>

  <div class="abs intro">
    <p>Navigating a diagnosis of dementia can be daunting. You likely have many questions, and it can be overwhelming trying to figure out where to turn to for answers and help. We want you to know that you are not alone in this journey.</p>
    <p>As the numbers of those living with dementia in Bermuda continue to rise placing greater demands on an already strained health care system, Willowmere's clinical and evidence based consultation services improve the safety, independence and quality of life of persons with dementia and their caregivers. Our goal is to assist clients to successfully age in place at home with the support of their family caregivers to reduce the overall cost and burden of care for this vulnerable population.</p>
  </div>

  <h2 class="abs fees-title">SERVICE <span class="script">Fees</span></h2>

  <div class="abs fee-card" style="left:36px;top:545px;width:143px;height:113px"><div class="fee-label">Initial<br>Consultation</div><div class="fee-price">$180</div></div>
  <div class="abs fee-card fee-card--gold" style="left:199px;top:545px;width:143px;height:113px"><div class="fee-label">Monthly check<br>in/monitoring<br>visits</div><div class="fee-price">$180</div></div>
  <div class="abs fee-card" style="left:358px;top:545px;width:143px;height:113px"><div class="fee-label">Comprehensive<br>Dementia<br>Assessment</div><div class="fee-price">$395</div></div>
  <div class="abs fee-card fee-card--gold" style="left:36px;top:678px;width:221px;height:112px"><div class="fee-label">Cognitive<br>Stimulation<br>Therapy</div><div class="fee-price">($500<span class="per-term">per<br>term</span>)</div></div>
  <div class="abs fee-card fee-card--gold" style="left:279px;top:678px;width:222px;height:112px"><div class="fee-label">Comprehensive Dementia<br>Assessment &amp; ongoing case<br>management services</div><div class="fee-price">$720</div></div>

  <p class="abs coverage">We are pleased to share that services offered by Willowmere Dementia are currently covered under Harbourline and Coralbay health insurance plans. We also have availability of funding support for those in financial need who are unable to afford co-pay, enabling equitable access to these essential care and support services regardless of financial means.</p>

  <p class="abs reach-out">Please feel free to reach out for<br>further information.</p>

  <div class="abs footer-band" style="top:1032px;height:114px"></div>
  <div class="abs phone-pill" style="left:111px;top:1018px">
    <span class="phone-icon"><svg width="20" height="20" viewBox="0 0 24 24"><path d="M6.6 10.8a15 15 0 0 0 6.6 6.6l2.2-2.2a1 1 0 0 1 1-.25 11.4 11.4 0 0 0 3.6.57 1 1 0 0 1 1 1V20a1 1 0 0 1-1 1A17 17 0 0 1 3 4a1 1 0 0 1 1-1h3.5a1 1 0 0 1 1 1c0 1.25.2 2.45.57 3.57a1 1 0 0 1-.25 1Z" fill="#1f1c6e"/></svg></span>(441) 555 0142
  </div>
  <div class="abs contact-line" style="top:1084px">
    <svg width="15" height="11" viewBox="0 0 15 11"><rect width="15" height="11" rx="1" fill="#f2a024"/><path d="M0 1l7.5 5L15 1" stroke="#1f1c6e" stroke-width="1.3" fill="none"/></svg>info@willowmeredementia.bm
    <svg width="15" height="15" viewBox="0 0 16 16" style="margin-left:6px"><circle cx="8" cy="8" r="7" stroke="#f2a024" stroke-width="1.4" fill="none"/><ellipse cx="8" cy="8" rx="3" ry="7" stroke="#f2a024" stroke-width="1.2" fill="none"/><path d="M1 8h14M2.5 4.5h11M2.5 11.5h11" stroke="#f2a024" stroke-width="1.1"/></svg>www.willowmeredementia.bm
  </div>
</section>

</body>
</html>
```